Business Card, Stationary, Envelope
Biz Cd/Stationary 4 ClinicPathwise
Business Card, Stationary, Envelope -
Creative Brief
Professional
Derek Sorvano
President
387 Harmon Ridge, #2214 Willowbrook, IL 60419
dsorvano@ClinicPathwise-example.com
www.ClinicPathwise-example.com
Clean appearance for medical practice consulting firm... tagline is "Evaluate. Implement. Thrive." although not sure that will fit on card. FYI....Skills of corporation are performance improvement, information systems evaluation. change emnagement, leadership, marketing...so kind of looking for kind of cutting edge/forward thinking, but definitely professional appearance

```html
<!DOCTYPE html>
<html lang="en">
<head>
<meta charset="utf-8">
<title>ClinicPathwise Stationery Concepts</title>
<link href="https://fonts.googleapis.com/css2?family=Open+Sans:wght@400;600;700&display=swap" rel="stylesheet">
<style>
  :root {
    --navy: #1c3f7c;
    --blue: #2a6fc0;
    --green: #5cb531;
    --lime: #9fd15a;
    --paper: #ffffff;
    --backdrop: #dccdb2;
    --ink: #4a4a4a;
    --muted: #8a8a8a;
    --shadow: rgba(0,0,0,0.2);
  }
  * { box-sizing: border-box; margin: 0; padding: 0; }
  html, body { width: 1200px; height: 432px; overflow: hidden; background: var(--paper); }
  body { font-family: "Open Sans", Arial, sans-serif; color: var(--ink); position: relative; }

  .logo-sheet { position: absolute; left: 0; top: 0; width: 318px; height: 432px; background: var(--paper); }
  .logo-option { position: absolute; left: 19px; width: 216px; height: 55px; display: flex; flex-direction: column; justify-content: center; padding-left: 6px; }
  .logo-option .wordmark { display: flex; align-items: center; gap: 5px; font-weight: 600; font-size: 22px; letter-spacing: -0.4px; line-height: 1; }
  .logo-option .wordmark .dot { width: 7px; height: 7px; border-radius: 50%; background: currentColor; }
  .logo-option .tagline { font-size: 7px; letter-spacing: 1.6px; margin-top: 3px; padding-left: 12px; color: var(--muted); }
  .opt-1 { top: 82px; } .opt-1 .wordmark { color: var(--navy); }
  .opt-2 { top: 152px; } .opt-2 .wordmark { color: var(--green); }
  .opt-3 { top: 222px; } .opt-3 .wordmark { color: var(--lime); }
  .opt-4 { top: 293px; background: var(--navy); } .opt-4 .wordmark, .opt-4 .tagline { color: #fff; }
  .option-number { position: absolute; left: 265px; font-size: 20px; line-height: 1; color: var(--navy); }

  .presentation { position: absolute; left: 318px; top: 0; width: 882px; height: 432px; background: var(--backdrop); }
  .sheet { position: absolute; background: var(--paper); box-shadow: 0 2px 5px var(--shadow); overflow: hidden; }
  .caption { position: absolute; font-size: 5px; letter-spacing: 0.6px; color: #7d715c; text-transform: uppercase; white-space: nowrap; }

  .mini-mark { display: flex; align-items: center; gap: 2px; font-weight: 600; color: var(--navy); line-height: 1; white-space: nowrap; }
  .mini-mark .dot { border-radius: 50%; background: var(--navy); }

  .card-front { left: 18px; top: 149px; width: 89px; height: 55px; }
  .card-front .mini-mark { position: absolute; left: 6px; top: 7px; font-size: 7px; }
  .card-front .mini-mark .dot { width: 3px; height: 3px; }
  .card-front .details { position: absolute; left: 6px; top: 22px; font-size: 2.8px; line-height: 1.5; }
  .card-front .band { position: absolute; left: 0; right: 0; bottom: 0; height: 3px; background: linear-gradient(90deg, var(--green), var(--blue)); }

  .card-back { left: 18px; top: 230px; width: 89px; height: 48px; display: flex; align-items: center; justify-content: center; }
  .card-back .mini-mark { font-size: 8px; }
  .card-back .mini-mark .dot { width: 3px; height: 3px; }

  .letterhead { left: 174px; top: 24px; width: 180px; height: 372px; }
  .letterhead .mini-mark { position: absolute; left: 10px; top: 12px; font-size: 8px; }
  .letterhead .mini-mark .dot { width: 3px; height: 3px; }
  .letterhead .address { position: absolute; left: 104px; top: 11px; font-size: 3px; line-height: 1.5; }
  .letterhead .faint-name { position: absolute; left: 0; right: 0; top: 168px; text-align: center; font-size: 18px; font-weight: 600; color: var(--navy); opacity: 0.06; }
  .letterhead .band { position: absolute; right: 0; bottom: 8px; width: 68px; height: 4px; background: linear-gradient(90deg, var(--green), var(--blue)); }
  .letterhead .footer { position: absolute; left: 10px; bottom: 8px; font-size: 3px; color: var(--muted); }

  .envelope-back svg { display: block; }
  .env-back-1 { left: 486px; top: 24px; width: 192px; height: 53px; }
  .env-back-2 { left: 486px; top: 91px; width: 192px; height: 58px; }

  .envelope-front .mini-mark { position: absolute; left: 8px; top: 9px; font-size: 6px; }
  .envelope-front .mini-mark .dot { width: 2.5px; height: 2.5px; }
  .envelope-front .return { position: absolute; left: 8px; top: 18px; font-size: 2.6px; color: var(--muted); white-space: nowrap; }
  .envelope-front .band { position: absolute; right: 0; bottom: 6px; width: 70px; height: 3px; background: linear-gradient(90deg, var(--green), var(--blue)); }
  .env-front-1 { left: 517px; top: 173px; width: 161px; height: 67px; }
  .env-front-2 { left: 474px; top: 252px; width: 204px; height: 137px; }
</style>
</head>
<body>
  <section class="logo-sheet">
    <div class="logo-option opt-1"><div class="wordmark"><span class="dot"></span>ClinicPathwise</div><div class="tagline">assess · improve · grow</div></div>
    <div class="option-number" style="top:100px">1</div>
    <div class="logo-option opt-2"><div class="wordmark"><span class="dot"></span>ClinicPathwise</div><div class="tagline">assess · improve · grow</div></div>
    <div class="option-number" style="top:170px">2</div>
    <div class="logo-option opt-3"><div class="wordmark"><span class="dot"></span>ClinicPathwise</div><div class="tagline">assess · improve · grow</div></div>
    <div class="option-number" style="top:240px">3</div>
    <div class="logo-option opt-4"><div class="wordmark"><span class="dot"></span>ClinicPathwise</div><div class="tagline">assess · improve · grow</div></div>
    <div class="option-number" style="top:311px">4</div>
  </section>

  <section class="presentation">
    <div class="caption" style="left:18px;top:141px">Stationery Concepts</div>

    <div class="sheet card-front">
      <div class="mini-mark"><span class="dot"></span>ClinicPathwise</div>
      <div class="details">Derek Sorvano · President<br>387 Harmon Ridge, #2214<br>Willowbrook, IL 60419<br>dsorvano@ClinicPathwise-example.com<br>www.ClinicPathwise-example.com</div>
      <div class="band"></div>
    </div>
    <div class="caption" style="left:18px;top:210px">Business Card Front</div>

    <div class="sheet card-back"><div class="mini-mark"><span class="dot"></span>ClinicPathwise</div></div>
    <div class="caption" style="left:18px;top:284px">Business Card Back</div>

    <div class="sheet letterhead">
      <div class="mini-mark"><span class="dot"></span>ClinicPathwise</div>
      <div class="address">387 Harmon Ridge, #2214<br>Willowbrook, IL 60419<br>dsorvano@ClinicPathwise-example.com<br>www.ClinicPathwise-example.com</div>
      <div class="faint-name">ClinicPathwise</div>
      <div class="footer">www.ClinicPathwise-example.com</div>
      <div class="band"></div>
    </div>
    <div class="caption" style="left:238px;top:402px">Letterhead Option</div>

    <div class="sheet envelope-back env-back-1">
      <svg width="192" height="53" viewBox="0 0 192 53"><rect width="192" height="53" fill="#fff"/><path d="M0 0 H192 V20 Q96 36 0 20 Z" fill="var(--blue)"/><path d="M0 20 Q96 36 192 20" stroke="var(--green)" stroke-width="2.5" fill="none"/></svg>
    </div>
    <div class="sheet envelope-back env-back-2">
      <svg width="192" height="58" viewBox="0 0 192 58"><rect width="192" height="58" fill="#fff"/><path d="M0 0 H192 V22 Q96 40 0 22 Z" fill="var(--green)"/></svg>
    </div>
    <div class="caption" style="left:556px;top:156px">Envelope Option</div>

    <div class="sheet envelope-front env-front-1">
      <div class="mini-mark"><span class="dot"></span>ClinicPathwise</div>
      <div class="return">387 Harmon Ridge, #2214 Willowbrook, IL 60419</div>
      <div class="band"></div>
    </div>
    <div class="sheet envelope-front env-front-2">
      <div class="mini-mark"><span class="dot"></span>ClinicPathwise</div>
      <div class="return">387 Harmon Ridge, #2214 Willowbrook, IL 60419</div>
      <div class="band"></div>
    </div>
  </section>
</body>
</html>
```